BRIGHTVALE MENTORING powerpoint deck.

I REQUIRE A COMPANY POWERPOINT SLIDE DECK, WHICH MAY ALSO INCLUDE A NUMBER OF "MODELS". THIS MAY ALSO REQUIRE SOME FOLLOW UP WORK.

ATTACHED IS AN EXAMPLE SLIDE DECK FOR ONE OF MY CLIENTS. I would like to see a mock up of a few slides and then i can send a complete deck over.

Please note my website... www.brightvalementoring.co.uk

I LOOK FORWARD TO SEEING YOUR DESIGN.

THANK YOU,

OWEN.

Target Market(s)

I work in the "learning and development"/ education/ leadership/ coaching industry

Industry/Entity Type

Leadership

Font styles to use
Other font styles liked:
• century gothic

Requirements
Must have
• ideally there would be some alignment to my website. www.brightvalementoring.co.uk
• be fresh, clean, simple enough. look professional.
Nice to have
• how you present "models" i would come back for more work in the future if the work is good.
Should not have
• too brash.

```html
<!DOCTYPE html>
<html lang="en">
<head>
<meta charset="utf-8">
<title>BRIGHTVALE MENTORING – Presentation Deck</title>
<link rel="stylesheet" href="https://fonts.googleapis.com/css2?family=Questrial&family=Raleway:wght@300;400;600&display=swap">
<style>
:root{
  --ink:#1a1a1a;--char:#2b2b2b;--slate:#4a4a4a;--grey:#8c8c8c;--mist:#dadada;--fog:#efefef;
  --teal:#7dc0bb;--teal-dark:#5aa39e;--paper:#ffffff;--canvas:#f3f3f3;
}
*{box-sizing:border-box;margin:0;padding:0}
html,body{width:1200px;height:4272px;overflow:hidden;background:var(--canvas)}
.deck{display:grid;grid-template-columns:repeat(3,386px);grid-auto-rows:217px;column-gap:12px;row-gap:20px;padding:12px 9px}
.slide{position:relative;overflow:hidden;background:var(--paper);color:var(--ink);font-family:'Questrial',sans-serif;box-shadow:0 1px 4px rgba(0,0,0,.18)}
.slide.dark{background:#141414;color:#fff}
.title{position:absolute;left:14px;top:11px;font-family:'Raleway',sans-serif;font-size:15px;font-weight:400}
.brand{position:absolute;right:12px;top:10px;font-size:7px;letter-spacing:1.5px;display:flex;align-items:center;gap:3px;color:var(--ink)}
.dark .brand,.brand.light{color:#fff}
.brand i{display:block;width:7px;height:7px;background:var(--teal)}
.foot{position:absolute;left:0;right:0;bottom:0;height:8px;background:var(--ink);color:#aaa;font-size:4px;line-height:8px;padding-left:6px}
.foot::after{content:"";position:absolute;right:0;top:0;width:22px;height:8px;background:var(--teal)}
.ph{position:absolute;background:linear-gradient(135deg,#6b6b6b,#2a2a2a)}
.ph.light{background:linear-gradient(135deg,#c9c9c9,#7d7d7d)}
.ph.warm{background:radial-gradient(circle at 50% 40%,#8a7a5a,#1c1c1c 70%)}
.abs{position:absolute}
.p{font-size:5.5px;line-height:1.55;color:var(--grey)}
.dark .p{color:#bdbdbd}
.h{font-size:8px;color:var(--ink)}
.dark .h{color:#fff}
.lead{font-size:9px;line-height:1.4;color:var(--ink)}
.sq{display:inline-block;width:9px;height:9px;background:var(--teal)}
.row{display:flex;align-items:center;gap:5px}
.dot{border-radius:50%}
.bigname{font-size:12px;letter-spacing:4px;color:#fff}
</style>
</head>
<body>
<main class="deck">

<!-- row 1 -->
<section class="slide dark">
  <div class="ph" style="inset:0;background:radial-gradient(circle at 50% 50%,#555,#0d0d0d 75%)" role="img" aria-label="Spiral staircase photograph in black and white"></div>
  <div class="abs" style="left:0;right:0;top:78px;text-align:center">
    <div class="row" style="justify-content:center"><i class="sq"></i><span class="bigname">BRIGHTVALE</span></div>
    <div style="font-size:6px;letter-spacing:3px;color:#ccc;margin-top:4px">MENTORING</div>
  </div>
</section>

<section class="slide">
  <div class="ph light" style="left:0;right:0;top:0;height:150px" role="img" aria-label="Group of business professionals in suits"></div>
  <div class="abs" style="left:0;right:0;top:150px;height:30px;background:var(--teal);color:#fff;text-align:center;font-size:13px;line-height:30px">Your Title Goes Here</div>
  <div class="brand" style="top:6px;left:170px;right:auto"><i></i>BRIGHTVALE</div>
  <div class="abs p" style="left:40px;right:40px;top:192px;display:flex;justify-content:space-between"><span>☏ 0100 000 000</span><span>✉ info@mail.com</span><span>⌂ brightvalementoring.co.uk</span></div>
  <div class="foot"></div>
</section>

<section class="slide dark">
  <div class="ph warm" style="inset:0" role="img" aria-label="Dim room with hanging light bulbs"></div>
  <div class="abs dot" style="left:236px;top:40px;width:26px;height:26px;background:var(--teal);color:#fff;text-align:center;font-size:18px;line-height:32px">“</div>
  <div class="abs" style="left:200px;top:74px;width:170px;font-size:9px;line-height:1.4;color:#fff">Coming together is a beginning. Keeping together is progress. Working together is success.</div>
  <div class="abs p" style="left:250px;top:118px">Alan Reeves</div>
</section>

<!-- row 2 -->
<section class="slide">
  <div class="title">Our Agenda</div><div class="brand"><i></i>BRIGHTVALE</div>
  <div class="abs" style="left:24px;top:50px;width:340px;display:grid;grid-template-columns:1fr 1fr;row-gap:26px;column-gap:30px">
    <div class="row"><i class="sq"></i><div><div class="h">Agenda One</div><div class="p">Short line of text here</div></div></div>
    <div class="row"><i class="sq" style="background:var(--ink)"></i><div><div class="h">Agenda Four</div><div class="p">Short line of text here</div></div></div>
    <div class="row"><i class="sq" style="background:var(--ink)"></i><div><div class="h">Agenda Two</div><div class="p">Short line of text here</div></div></div>
    <div class="row"><i class="sq"></i><div><div class="h">Agenda Five</div><div class="p">Short line of text here</div></div></div>
    <div class="row"><i class="sq"></i><div><div class="h">Agenda Three</div><div class="p">Short line of text here</div></div></div>
    <div class="row"><i class="sq" style="background:var(--ink)"></i><div><div class="h">Agenda Six</div><div class="p">Short line of text here</div></div></div>
  </div>
  <div class="foot">www.brightvalementoring.co.uk</div>
</section>

<section class="slide">
  <div class="ph light" style="left:0;top:0;bottom:8px;width:190px" role="img" aria-label="Business team standing together"></div>
  <div class="abs" style="left:190px;right:0;top:0;bottom:8px;background:var(--char)"></div>
  <div class="brand light"><i></i>BRIGHTVALE</div>
  <div class="abs" style="left:205px;top:60px;font-size:15px;color:#fff">About Us</div>
  <div class="abs p" style="left:205px;top:84px;width:160px;color:#bbb">A short paragraph describing who we are, how we work and the leaders we help to grow each year.</div>
  <div class="foot"></div>
</section>

<section class="slide">
  <div class="title">Our Services</div><div class="brand"><i></i>BRIGHTVALE</div>
  <div class="ph warm" style="left:14px;top:40px;width:200px;height:150px" role="img" aria-label="Glowing light bulbs on dark background"></div>
  <div class="abs" style="left:232px;top:52px;display:flex;flex-direction:column;gap:22px">
    <div class="row"><i class="sq"></i><div><div class="h">Service Number One</div><div class="p">Short line of text</div></div></div>
    <div class="row"><i class="sq"></i><div><div class="h">Service Number Two</div><div class="p">Short line of text</div></div></div>
    <div class="row"><i class="sq"></i><div><div class="h">Service Number Three</div><div class="p">Short line of text</div></div></div>
  </div>
  <div class="foot">www.brightvalementoring.co.uk</div>
</section>

<!-- row 3 -->
<section class="slide">
  <div class="title">Quote Area</div><div class="brand"><i></i>BRIGHTVALE</div>
  <div class="abs" style="left:0;top:40px;width:150px;height:140px;background:var(--char)"></div>
  <div class="abs" style="left:14px;top:60px;width:125px;font-size:8px;line-height:1.45;color:#fff">“Coming together is a beginning, keeping together is progress.”</div>
  <div class="abs p" style="left:14px;top:110px">Alan Reeves</div>
  <div class="ph light" style="left:150px;right:0;top:40px;height:140px" role="img" aria-label="Sailing boats racing on water"></div>
  <div class="foot"></div>
</section>

<section class="slide">
  <div class="abs" style="inset:14px 14px 20px;display:grid;grid-template-columns:repeat(4,1fr);grid-template-rows:repeat(3,1fr);gap:6px;font-size:10px;color:var(--slate);text-align:center;align-items:center">
    <div>Stonegate</div><div>Northway</div><div>Calder &amp; Co</div><div>Fenmoor</div>
    <div>Harlow Bank</div><div style="grid-column:span 2;grid-row:span 2;background:var(--ink);color:#fff;font-size:14px;height:100%;display:flex;align-items:center;justify-content:center">The Client</div><div>Aqualine</div>
    <div>Tvista</div><div>Athleta Union</div>
  </div>
  <div class="foot"></div>
</section>

<section class="slide">
  <div class="title">Text Area</div><div class="brand"><i></i>BRIGHTVALE</div>
  <div class="abs lead" style="left:14px;top:40px;width:340px">This is a place for your header text. Insert your best text here, just replace this text with your own text.</div>
  <div class="abs p" style="left:14px;top:72px;width:350px">Lorem ipsum dolor sit amet, consectetur adipiscing elit. Integer nec odio. Praesent libero. Sed cursus ante dapibus diam. Sed nisi. Nulla quis sem at nibh elementum imperdiet. Duis sagittis ipsum.<br><br>Praesent mauris. Fusce nec tellus sed augue semper porta. Mauris massa. Vestibulum lacinia arcu eget nulla. Class aptent taciti sociosqu ad litora torquent per conubia nostra.<br><br>Curabitur sodales ligula in libero. Sed dignissim lacinia nunc. Curabitur tortor. Pellentesque nibh. Aenean quam.</div>
  <div class="foot"></div>
</section>

<!-- row 4 -->
<section class="slide">
  <div class="title">Our Vision &amp; Mission</div><div class="brand"><i></i>BRIGHTVALE</div>
  <div class="ph" style="left:0;top:36px;width:180px;bottom:8px" role="img" aria-label="Business people in dark toned photo"></div>
  <div class="abs" style="left:12px;top:60px;color:#fff"><div style="font-size:10px">▪ Our Vision</div><div style="font-size:7px;margin-top:5px;line-height:1.4">Go to the Next Level.<br>Without look in the past</div></div>
  <div class="abs" style="left:196px;top:46px;font-size:10px">Our Missions</div>
  <div class="abs" style="left:196px;top:66px;display:flex;flex-direction:column;gap:12px">
    <div class="row"><i class="dot" style="width:12px;height:12px;background:var(--ink)"></i><span class="p">Mission text here</span></div>
    <div class="row"><i class="dot" style="width:12px;height:12px;background:var(--teal)"></i><span class="p">Mission text here</span></div>
    <div class="row"><i class="dot" style="width:12px;height:12px;background:var(--ink)"></i><span class="p">Mission text here</span></div>
    <div class="row"><i class="dot" style="width:12px;height:12px;background:var(--teal)"></i><span class="p">Mission text here</span></div>
  </div>
  <div class="foot"></div>
</section>

<section class="slide">
  <div class="abs" style="left:0;top:0;width:120px;bottom:8px;background:var(--ink)"></div>
  <div class="abs" style="left:120px;top:0;width:4px;bottom:8px;background:var(--teal)"></div>
  <div class="title" style="left:136px">Text Area</div><div class="brand"><i></i>BRIGHTVALE</div>
  <div class="abs lead" style="left:136px;top:40px;width:230px">This is a place for your header text. Insert your best text here, just replace this text with your own text.</div>
  <div class="abs p" style="left:136px;top:80px;width:236px">Lorem ipsum dolor sit amet, consectetur adipiscing elit. Integer nec odio. Praesent libero. Sed cursus ante dapibus diam. Sed nisi nulla quis sem.<br><br>Fusce nec tellus sed augue semper porta. Mauris massa vestibulum lacinia arcu eget nulla.</div>
  <div class="foot"></div>
</section>

<section class="slide">
  <div class="title">SWOT Analysis</div><div class="brand"><i></i>BRIGHTVALE</div>
  <svg class="abs" style="left:120px;top:50px" width="150" height="120" viewBox="0 0 150 120">
    <rect x="25" y="10" width="40" height="40" rx="20" fill="#7dc0bb"/><rect x="85" y="10" width="40" height="40" rx="20" fill="#1a1a1a"/>
    <rect x="25" y="65" width="40" height="40" rx="20" fill="#1a1a1a"/><rect x="85" y="65" width="40" height="40" rx="20" fill="#7dc0bb"/>
    <rect x="45" y="30" width="60" height="55" fill="#4a4a4a"/>
  </svg>
  <div class="abs" style="left:276px;top:56px"><div class="h">+ Strengths</div><div class="p">Short text here</div></div>
  <div class="abs" style="left:276px;top:116px"><div class="h">+ Weaknesses</div><div class="p">Short text here</div></div>
  <div class="abs" style="left:30px;top:70px"><div class="h">+ Threats</div><div class="p">Short text here</div></div>
  <div class="abs" style="left:30px;top:126px"><div class="h">+ Opportunities</div><div class="p">Short text here</div></div>
  <div class="foot"></div>
</section>

<!-- row 5 -->
<section class="slide">
  <div class="ph light" style="left:0;top:0;width:150px;bottom:8px" role="img" aria-label="Hands typing on a laptop"></div>
  <div class="brand"><i></i>BRIGHTVALE</div>
  <div class="abs" style="left:168px;top:50px;font-size:14px">Your Title Goes Here</div>
  <div class="abs" style="left:168px;top:80px;display:flex;flex-direction:column;gap:14px">
    <div class="row"><i class="sq" style="background:var(--ink)"></i><div><div class="h">Your Text Here</div><div class="p">Short line of placeholder text</div></div></div>
    <div class="row"><i class="sq" style="background:var(--ink)"></i><div><div class="h">Your Text Here</div><div class="p">Short line of placeholder text</div></div></div>
  </div>
  <div class="foot"></div>
</section>

<section class="slide">
  <div class="title">Your Title Goes Here</div><div class="brand"><i></i>BRIGHTVALE</div>
  <div class="ph light" style="left:14px;top:40px;width:110px;height:60px" role="img" aria-label="Business team photo"></div>
  <div class="abs" style="left:130px;top:40px;width:110px;height:60px;background:var(--teal)"></div>
  <div class="ph light" style="left:246px;top:40px;width:126px;height:60px" role="img" aria-label="Business people photo"></div>
  <div class="abs" style="left:14px;top:106px;width:110px;height:76px;background:var(--ink)"></div>
  <div class="ph light" style="left:130px;top:106px;width:110px;height:76px" role="img" aria-label="Chess pieces photo"></div>
  <div class="abs" style="left:246px;top:106px;width:126px;height:76px;background:var(--fog)"></div>
  <div class="abs" style="left:20px;top:112px;color:#fff;font-size:7px">Heading Goes Here</div>
  <div class="abs p" style="left:252px;top:112px;width:114px">Short text for this box here</div>
  <div class="foot"></div>
</section>

<section class="slide dark">
  <div class="ph" style="left:0;top:0;width:190px;bottom:0" role="img" aria-label="Staircase leading upward"></div>
  <div class="abs" style="left:204px;top:24px;width:170px;font-size:9px;line-height:1.4">This is place for your header text. Insert your best text here, just replace</div>
  <div class="abs" style="left:204px;top:74px;display:flex;flex-direction:column;gap:11px">
    <div class="row"><span style="font-size:8px">✎</span><span class="p">Your Text Here</span></div>
    <div class="row"><span style="font-size:8px">✎</span><span class="p">Your Text Here</span></div>
    <div class="row"><span style="font-size:8px">✎</span><span class="p">Your Text Here</span></div>
    <div class="row"><span style="font-size:8px">✎</span><span class="p">Your Text Here</span></div>
  </div>
</section>

<!-- row 6 -->
<section class="slide">
  <div class="ph light" style="left:0;top:0;width:110px;bottom:8px" role="img" aria-label="Team hands stacked together"></div>
  <div class="ph light" style="left:112px;top:0;width:110px;bottom:8px" role="img" aria-label="Team hands stacked together close-up"></div>
  <div class="abs row" style="left:18px;top:24px"><i class="sq"></i><span style="font-size:8px;color:#fff;letter-spacing:1px">BRIGHTVALE</span></div>
  <div class="abs" style="left:240px;top:60px;font-size:14px;line-height:1.3">Your Title<br>Goes Here</div>
  <div class="abs p" style="left:240px;top:104px;width:130px">Short supporting text here</div>
  <div class="foot"></div>
</section>

<section class="slide">
  <div class="title">Your Title Goes Here</div><div class="brand"><i></i>BRIGHTVALE</div>
  <div class="abs lead" style="left:14px;top:40px;width:150px">This is a place for your header text. Insert your best text here.</div>
  <div class="abs p" style="left:14px;top:82px;width:150px">Lorem ipsum dolor sit amet, consectetur adipiscing elit. Integer nec odio praesent libero sed cursus ante.</div>
  <div class="ph" style="left:180px;top:40px;width:60px;height:150px" role="img" aria-label="Chess piece on dark background"></div>
  <div class="ph" style="left:244px;top:40px;width:60px;height:150px" role="img" aria-label="Chess piece on dark background"></div>
  <div class="ph" style="left:308px;top:40px;width:64px;height:150px" role="img" aria-label="Chess piece on dark background"></div>
  <div class="foot"></div>
</section>

<section class="slide">
  <div class="title">Our Differences</div><div class="brand"><i></i>BRIGHTVALE</div>
  <div class="abs" style="left:0;right:0;top:40px;height:140px;background:var(--ink)"></div>
  <div class="ph" style="left:230px;right:0;top:40px;height:140px" role="img" aria-label="Chess pieces in silhouette"></div>
  <div class="abs" style="left:14px;top:52px;display:flex;flex-direction:column;gap:10px;color:#fff">
    <div class="row"><i class="dot" style="width:11px;height:11px;background:var(--teal)"></i><span style="font-size:6px;color:#ccc">Text about the first point here</span></div>
    <div class="row"><i class="dot" style="width:11px;height:11px;background:var(--teal)"></i><span style="font-size:6px;color:#ccc">Text about the second point here</span></div>
    <div class="row"><i class="dot" style="width:11px;height:11px;background:var(--teal)"></i><span style="font-size:6px;color:#ccc">Text about the third point here</span></div>
    <div class="row"><i class="dot" style="width:11px;height:11px;background:var(--teal)"></i><span style="font-size:6px;color:#ccc">Text about the fourth point here</span></div>
  </div>
  <div class="foot"></div>
</section>

<!-- row 7 -->
<section class="slide">
  <div class="title">Two Column Description</div><div class="brand"><i></i>BRIGHTVALE</div>
  <div class="abs lead" style="left:14px;top:40px;width:320px">This is a place for your header text. Insert your best text here, just replace this text with your own text.</div>
  <div class="abs p" style="left:14px;top:80px;width:170px">Lorem ipsum dolor sit amet, consectetur adipiscing elit. Integer nec odio. Praesent libero sed cursus ante dapibus diam. Sed nisi nulla quis sem.</div>
  <div class="abs p" style="left:200px;top:80px;width:170px">Lorem ipsum dolor sit amet, consectetur adipiscing elit. Integer nec odio. Praesent libero sed cursus ante dapibus diam. Sed nisi nulla quis sem.</div>
  <div class="foot"></div>
</section>

<section class="slide dark">
  <div class="ph" style="inset:0;background:linear-gradient(180deg,#2a2a2a,#0e0e0e)" role="img" aria-label="Coffee cup on dark table"></div>
  <div class="brand light" style="left:165px;right:auto;top:20px"><i></i>BRIGHTVALE</div>
  <div class="abs" style="left:14px;top:150px;font-size:11px;letter-spacing:1px">COFFEE BREAK</div>
  <div class="abs p" style="left:14px;top:166px">Back in 15 minutes</div>
</section>

<section class="slide">
  <div class="title">Three Column Description</div><div class="brand"><i></i>BRIGHTVALE</div>
  <div class="abs lead" style="left:14px;top:40px;width:320px">This is a place for your header text. Insert your best text here, just replace this text with your own text.</div>
  <div class="abs p" style="left:14px;top:80px;width:110px">Lorem ipsum dolor sit amet, consectetur adipiscing elit integer nec odio.</div>
  <div class="abs p" style="left:138px;top:80px;width:110px">Lorem ipsum dolor sit amet, consectetur adipiscing elit integer nec odio.</div>
  <div class="abs p" style="left:262px;top:80px;width:110px">Lorem ipsum dolor sit amet, consectetur adipiscing elit integer nec odio.</div>
  <div class="foot"></div>
</section>

<!-- row 8 -->
<section class="slide dark">
  <div class="ph" style="inset:0" role="img" aria-label="Abstract dark architectural photo"></div>
  <div class="abs row" style="left:140px;top:24px"><i class="sq"></i><span style="font-size:9px;letter-spacing:2px">BRIGHTVALE</span></div>
  <div class="abs" style="left:24px;top:120px;font-size:13px;line-height:1.3">Your Title<br>Goes Here</div>
</section>

<section class="slide">
  <div class="title">Your Title Goes Here</div><div class="brand"><i></i>BRIGHTVALE</div>
  <div class="abs" style="left:14px;top:48px;display:flex;flex-direction:column;gap:18px">
    <div class="row"><i class="dot" style="width:12px;height:12px;background:var(--teal)"></i><div><div class="h">Service Number One</div><div class="p">Short text here</div></div></div>
    <div class="row"><i class="dot" style="width:12px;height:12px;background:var(--teal)"></i><div><div class="h">Service Number Two</div><div class="p">Short text here</div></div></div>
    <div class="row"><i class="dot" style="width:12px;height:12px;background:var(--teal)"></i><div><div class="h">Service Number Three</div><div class="p">Short text here</div></div></div>
  </div>
  <div class="abs" style="left:196px;top:44px;width:176px;display:flex;flex-direction:column;gap:6px">
    <div class="row" style="background:var(--ink);color:#fff;height:42px;padding:0 10px"><span style="font-size:18px">1</span><span style="font-size:6px;color:#ccc">Your text goes here</span></div>
    <div class="row" style="background:var(--teal);color:#fff;height:42px;padding:0 10px"><span style="font-size:18px">2</span><span style="font-size:6px">Your text goes here</span></div>
    <div class="row" style="background:var(--slate);color:#fff;height:42px;padding:0 10px"><span style="font-size:18px">3</span><span style="font-size:6px;color:#ddd">Your text goes here</span></div>
  </div>
  <div class="foot"></div>
</section>

<section class="slide">
  <div class="title">Four Bullets with Paragraph</div><div class="brand"><i></i>BRIGHTVALE</div>
  <div class="abs" style="left:14px;top:50px;display:grid;grid-template-columns:1fr 1fr;gap:22px 18px;width:210px">
    <div class="row"><i class="dot" style="width:12px;height:12px;background:var(--teal)"></i><div><div class="h">Your Text</div><div class="p">Short text</div></div></div>
    <div class="row"><i class="dot" style="width:12px;height:12px;background:var(--teal)"></i><div><div class="h">Your Text</div><div class="p">Short text</div></div></div>
    <div class="row"><i class="dot" style="width:12px;height:12px;background:var(--teal)"></i><div><div class="h">Your Text</div><div class="p">Short text</div></div></div>
    <div class="row"><i class="dot" style="width:12px;height:12px;background:var(--teal)"></i><div><div class="h">Your Text</div><div class="p">Short text</div></div></div>
  </div>
  <div class="abs" style="left:240px;top:52px;width:132px"><div class="h">Heading Goes Here</div><div class="p" style="margin-top:6px">Lorem ipsum dolor sit amet, consectetur adipiscing elit. Integer nec odio praesent libero sed cursus.</div></div>
  <div class="foot"></div>
</section>

<!-- row 9 -->
<section class="slide">
  <div class="title">Your Title</div><div class="brand"><i></i>BRIGHTVALE</div>
  <div class="abs" style="left:14px;top:40px;width:120px"><div class="h">Heading Goes Here</div><div class="p" style="margin-top:5px">Lorem ipsum dolor sit amet, consectetur adipiscing elit integer nec.</div></div>
  <div class="ph light" style="left:140px;top:36px;width:110px;bottom:8px" role="img" aria-label="Light bulb close-up"></div>
  <div class="abs" style="left:262px;top:50px;display:flex;flex-direction:column;gap:14px">
    <div class="row"><i class="dot" style="width:11px;height:11px;background:var(--teal)"></i><span class="p">Your Text Here</span></div>
    <div class="row"><i class="dot" style="width:11px;height:11px;background:var(--teal)"></i><span class="p">Your Text Here</span></div>
    <div class="row"><i class="dot" style="width:11px;height:11px;background:var(--teal)"></i><span class="p">Your Text Here</span></div>
    <div class="row"><i class="dot" style="width:11px;height:11px;background:var(--teal)"></i><span class="p">Your Text Here</span></div>
  </div>
  <div class="foot"></div>
</section>

<section class="slide">
  <div class="title">Text &amp; Bullet Area</div><div class="brand"><i></i>BRIGHTVALE</div>
  <div class="abs" style="left:14px;top:44px;width:140px"><div class="h">Heading Goes Here</div><div class="p" style="margin-top:5px">Lorem ipsum dolor sit amet, consectetur adipiscing elit. Integer nec odio praesent libero sed cursus ante dapibus.</div></div>
  <div class="abs" style="left:176px;top:46px;display:grid;grid-template-columns:1fr 1fr;gap:14px 14px">
    <div class="row"><i class="dot" style="width:11px;height:11px;background:var(--teal)"></i><span class="p">Your Text</span></div>
    <div class="row"><i class="dot" style="width:11px;height:11px;background:var(--ink)"></i><span class="p">Your Text</span></div>
    <div class="row"><i class="dot" style="width:11px;height:11px;background:var(--ink)"></i><span class="p">Your Text</span></div>
    <div class="row"><i class="dot" style="width:11px;height:11px;background:var(--teal)"></i><span class="p">Your Text</span></div>
    <div class="row"><i class="dot" style="width:11px;height:11px;background:var(--teal)"></i><span class="p">Your Text</span></div>
    <div class="row"><i class="dot" style="width:11px;height:11px;background:var(--ink)"></i><span class="p">Your Text</span></div>
  </div>
  <div class="foot"></div>
</section>

<section class="slide dark">
  <div class="ph warm" style="inset:0" role="img" aria-label="Hanging vintage light bulbs"></div>
  <div class="brand light"><i></i>BRIGHTVALE</div>
  <div class="abs" style="left:150px;top:96px;font-size:14px">Your Title Goes Here</div>
  <div class="abs p" style="left:150px;top:116px">Short subtitle text here</div>
</section>

<!-- row 10 -->
<section class="slide">
  <div class="title">Paragraph with Three Bullet</div><div class="brand"><i></i>BRIGHTVALE</div>
  <div class="abs lead" style="left:14px;top:40px;width:330px">This is a place for your header text. Insert your best text here, just replace this text with your own text.</div>
  <div class="abs" style="left:14px;top:96px;width:358px;display:flex;justify-content:space-around;text-align:center">
    <div><i class="dot" style="display:block;margin:0 auto 6px;width:18px;height:18px;background:var(--teal)"></i><div class="h">Your Text</div><div class="p">Short text</div></div>
    <div><i class="dot" style="display:block;margin:0 auto 6px;width:18px;height:18px;background:var(--teal)"></i><div class="h">Your Text</div><div class="p">Short text</div></div>
    <div><i class="dot" style="display:block;margin:0 auto 6px;width:18px;height:18px;background:var(--teal)"></i><div class="h">Your Text</div><div class="p">Short text</div></div>
  </div>
  <div class="foot"></div>
</section>

<section class="slide">
  <div class="title">Multiple Column Area</div><div class="brand"><i></i>BRIGHTVALE</div>
  <div class="abs" style="left:14px;top:44px;width:358px;display:flex;justify-content:space-around;text-align:center">
    <div><div style="color:var(--teal);font-size:11px">✔</div><div class="p">Text Here</div></div>
    <div><div style="color:var(--teal);font-size:11px">✔</div><div class="p">Text Here</div></div>
    <div><div style="color:var(--teal);font-size:11px">✔</div><div class="p">Text Here</div></div>
    <div><div style="color:var(--teal);font-size:11px">✔</div><div class="p">Text Here</div></div>
  </div>
  <div class="abs" style="left:14px;top:100px;width:160px"><div class="h">Heading Goes Here</div><div class="p" style="margin-top:4px">Lorem ipsum dolor sit amet, consectetur adipiscing elit integer nec odio.</div></div>
  <div class="abs" style="left:200px;top:100px;width:160px"><div class="h">Heading Goes Here</div><div class="p" style="margin-top:4px">Lorem ipsum dolor sit amet, consectetur adipiscing elit integer nec odio.</div></div>
  <div class="foot"></div>
</section>

<section class="slide">
  <div class="title">Monthly Subscription</div><div class="brand"><i></i>BRIGHTVALE</div>
  <div class="abs" style="left:0;right:0;top:110px;bottom:8px;background:var(--ink)"></div>
  <div class="abs" style="left:40px;top:44px;width:90px;height:120px;background:#fff;box-shadow:0 1px 3px rgba(0,0,0,.3);text-align:center;padding-top:8px"><div style="font-size:12px">$100</div><div class="p" style="margin-top:8px">Basic plan<br>Feature one<br>Feature two</div></div>
  <div class="abs" style="left:148px;top:38px;width:90px;height:132px;background:var(--ink);color:#fff;text-align:center;padding-top:10px;box-shadow:0 1px 4px rgba(0,0,0,.4)"><div style="font-size:13px">$200</div><div class="p" style="margin-top:8px">Standard plan<br>Feature one<br>Feature two</div></div>
  <div class="abs" style="left:256px;top:44px;width:90px;height:120px;background:var(--teal);color:#fff;text-align:center;padding-top:8px"><div style="font-size:12px">$400</div><div style="font-size:5.5px;line-height:1.55;margin-top:8px">Premium plan<br>Feature one<br>Feature two</div></div>
  <div class="foot"></div>
</section>

<!-- row 11 -->
<section class="slide dark">
  <div class="ph" style="inset:0;background:radial-gradient(circle at 50% 50%,#4d4d4d,#0d0d0d 75%)" role="img" aria-label="Spiral staircase photograph"></div>
  <div class="abs row" style="left:150px;top:30px"><i class="sq"></i><span style="font-size:9px;letter-spacing:2px">BRIGHTVALE</span></div>
  <div class="abs" style="left:24px;top:110px;font-size:14px">Your Title Goes Here</div>
  <div class="abs p" style="left:24px;top:130px">Short subtitle text</div>
</section>

<section class="slide">
  <div class="brand"><i></i>BRIGHTVALE</div>
  <div class="abs" style="left:14px;top:30px;font-size:14px;line-height:1.3">Video Title<br>Goes Here</div>
  <div class="abs p" style="left:14px;top:70px;width:100px">Short supporting text for the video here.</div>
  <div class="abs" style="left:128px;top:30px;width:244px;height:140px;background:var(--ink);padding:6px"><div class="ph light" style="position:relative;width:100%;height:100%" role="img" aria-label="Video still of business team"></div></div>
  <div class="abs" style="left:240px;top:88px;width:22px;height:16px;background:var(--teal);border-radius:4px"></div>
  <svg class="abs" style="left:247px;top:91px" width="10" height="10" viewBox="0 0 10 10"><path d="M2 1 L9 5 L2 9Z" fill="#fff"/></svg>
  <div class="abs" style="left:230px;top:170px;width:40px;height:14px;background:var(--mist)"></div>
  <div class="foot"></div>
</section>

<section class="slide">
  <div class="title">Four Column Area</div><div class="brand"><i></i>BRIGHTVALE</div>
  <div class="abs" style="left:14px;top:46px;width:358px;height:130px;display:grid;grid-template-columns:repeat(4,1fr);gap:6px">
    <div style="background:var(--ink);color:#fff;padding:10px;text-align:center"><div style="font-size:12px">✔</div><div style="font-size:6px;margin-top:20px">Your Text Here</div></div>
    <div style="background:var(--teal);color:#fff;padding:10px;text-align:center"><div style="font-size:12px">✔</div><div style="font-size:6px;margin-top:20px">Your Text Here</div></div>
    <div style="background:var(--slate);color:#fff;padding:10px;text-align:center"><div style="font-size:12px">✔</div><div style="font-size:6px;margin-top:20px">Your Text Here</div></div>
    <div style="background:var(--ink);color:#fff;padding:10px;text-align:center"><div style="font-size:12px">✔</div><div style="font-size:6px;margin-top:20px">Your Text Here</div></div>
  </div>
  <div class="foot"></div>
</section>

<!-- row 12 -->
<section class="slide">
  <div class="title">Four Column Area</div><div class="brand"><i></i>BRIGHTVALE</div>
  <div class="abs" style="left:14px;top:50px;width:358px;display:flex;justify-content:space-around;text-align:center">
    <div><i class="dot" style="display:block;margin:0 auto 8px;width:40px;height:40px;background:var(--ink)"></i><div class="h">COLUMN 1</div><div class="p">Short text</div></div>
    <div><i class="dot" style="display:block;margin:0 auto 8px;width:40px;height:40px;background:var(--teal)"></i><div class="h">COLUMN 2</div><div class="p">Short text</div></div>
    <div><i class="dot" style="display:block;margin:0 auto 8px;width:40px;height:40px;background:var(--slate)"></i><div class="h">COLUMN 3</div><div class="p">Short text</div></div>
    <div><i class="dot" style="display:block;margin:0 auto 8px;width:40px;height:40px;background:var(--ink)"></i><div class="h">COLUMN 4</div><div class="p">Short text</div></div>
  </div>
  <div class="foot"></div>
</section>

<section class="slide">
  <div class="title">Key Points Area</div><div class="brand"><i></i>BRIGHTVALE</div>
  <div class="abs" style="left:20px;right:20px;top:80px;height:2px;background:var(--teal)"></div>
  <div class="abs" style="left:20px;top:58px;width:346px;display:flex;justify-content:space-between;text-align:center">
    <div><i class="dot" style="display:block;margin:0 auto 8px;width:44px;height:44px;background:var(--ink)"></i><div class="p">Key point text</div></div>
    <div><i class="dot" style="display:block;margin:0 auto 8px;width:44px;height:44px;background:var(--ink)"></i><div class="p">Key point text</div></div>
    <div><i class="dot" style="display:block;margin:0 auto 8px;width:44px;height:44px;background:var(--ink)"></i><div class="p">Key point text</div></div>
    <div><i class="dot" style="display:block;margin:0 auto 8px;width:44px;height:44px;background:var(--ink)"></i><div class="p">Key point text</div></div>
  </div>
  <div class="foot"></div>
</section>

<section class="slide">
  <div class="title">Workflow Area</div><div class="brand"><i></i>BRIGHTVALE</div>
  <svg class="abs" style="left:20px;top:50px" width="346" height="90" viewBox="0 0 346 90">
    <g fill="none" stroke-width="14">
      <path d="M10 60 A33 33 0 0 1 76 60" stroke="#1a1a1a"/>
      <path d="M76 30 A33 33 0 0 0 142 30" stroke="#7dc0bb"/>
      <path d="M142 60 A33 33 0 0 1 208 60" stroke="#1a1a1a"/>
      <path d="M208 30 A33 33 0 0 0 274 30" stroke="#7dc0bb"/>
      <path d="M274 60 A33 33 0 0 1 340 60" stroke="#1a1a1a"/>
    </g>
  </svg>
  <div class="abs" style="left:20px;top:150px;width:346px;display:flex;justify-content:space-between" ><span class="p">Step One</span><span class="p">Step Two</span><span class="p">Step Three</span><span class="p">Step Four</span><span class="p">Step Five</span></div>
  <div class="foot"></div>
</section>

<!-- row 13 -->
<section class="slide">
  <div class="title">Timeline</div><div class="brand"><i></i>BRIGHTVALE</div>
  <div class="abs" style="left:20px;right:20px;top:80px;height:2px;background:var(--mist)"></div>
  <div class="abs" style="left:30px;top:64px;width:326px;display:flex;justify-content:space-between;text-align:center">
    <div><i class="dot" style="display:block;margin:0 auto 6px;width:34px;height:34px;background:var(--ink)"></i><div class="h">2015</div><div class="p">Short text</div></div>
    <div><i class="dot" style="display:block;margin:0 auto 6px;width:34px;height:34px;background:var(--teal)"></i><div class="h">2016</div><div class="p">Short text</div></div>
    <div><i class="dot" style="display:block;margin:0 auto 6px;width:34px;height:34px;background:var(--ink)"></i><div class="h">2017</div><div class="p">Short text</div></div>
    <div><i class="dot" style="display:block;margin:0 auto 6px;width:34px;height:34px;background:var(--teal)"></i><div class="h">2018</div><div class="p">Short text</div></div>
  </div>
  <div class="foot"></div>
</section>

<section class="slide">
  <div class="title">This Is Line Chart Slide</div><div class="brand"><i></i>BRIGHTVALE</div>
  <svg class="abs" style="left:40px;top:44px" width="306" height="140" viewBox="0 0 306 140">
    <g stroke="#e4e4e4"><line x1="0" y1="20" x2="306" y2="20"/><line x1="0" y1="60" x2="306" y2="60"/><line x1="0" y1="100" x2="306" y2="100"/><line x1="0" y1="130" x2="306" y2="130"/></g>
    <polyline points="10,40 90,110 170,30 250,70 300,50" fill="none" stroke="#1a1a1a" stroke-width="2"/>
    <polyline points="10,100 90,50 170,90 250,20 300,80" fill="none" stroke="#7dc0bb" stroke-width="2"/>
  </svg>
  <div class="foot"></div>
</section>

<section class="slide">
  <div class="title">Market Performance</div><div class="brand"><i></i>BRIGHTVALE</div>
  <svg class="abs" style="left:20px;top:50px" width="346" height="120" viewBox="0 0 346 120">
    <line x1="0" y1="110" x2="346" y2="110" stroke="#ccc"/>
    <g fill="#1a1a1a"><rect x="20" y="40" width="14" height="70"/><rect x="100" y="20" width="14" height="90"/><rect x="180" y="50" width="14" height="60"/><rect x="260" y="30" width="14" height="80"/></g>
    <g fill="#7dc0bb"><rect x="36" y="60" width="14" height="50"/><rect x="116" y="45" width="14" height="65"/><rect x="196" y="25" width="14" height="85"/><rect x="276" y="55" width="14" height="55"/></g>
    <g fill="#8c8c8c"><rect x="52" y="75" width="14" height="35"/><rect x="132" y="70" width="14" height="40"/><rect x="212" y="65" width="14" height="45"/><rect x="292" y="80" width="14" height="30"/></g>
  </svg>
  <div class="foot"></div>
</section>

<!-- row 14 -->
<section class="slide">
  <div class="title">Market Performance</div><div class="brand"><i></i>BRIGHTVALE</div>
  <svg class="abs" style="left:20px;top:44px" width="346" height="110" viewBox="0 0 346 110">
    <g fill="#1a1a1a"><rect x="20" y="40" width="40" height="70"/><rect x="100" y="20" width="40" height="90"/><rect x="180" y="10" width="40" height="100"/><rect x="260" y="50" width="40" height="60"/></g>
    <g fill="#7dc0bb"><rect x="60" y="60" width="14" height="50"/><rect x="140" y="50" width="14" height="60"/><rect x="220" y="35" width="14" height="75"/><rect x="300" y="70" width="14" height="40"/></g>
  </svg>
  <div class="abs row" style="left:20px;top:168px"><i class="dot" style="width:14px;height:14px;background:var(--ink)"></i><div><div class="h">Your Text Here</div><div class="p">Short text</div></div></div>
  <div class="foot"></div>
</section>

<section class="slide">
  <div class="title">Our Team</div><div class="brand"><i></i>BRIGHTVALE</div>
  <div class="abs" style="left:30px;top:44px;display:grid;grid-template-columns:1fr 1fr;gap:16px 40px">
    <div class="row"><div class="ph light" style="position:relative;width:34px;height:34px" role="img" aria-label="Team member portrait"></div><div><div class="h">Name Here</div><div class="p">Job title</div></div></div>
    <div class="row"><div class="ph light" style="position:relative;width:34px;height:34px" role="img" aria-label="Team member portrait"></div><div><div class="h">Name Here</div><div class="p">Job title</div></div></div>
    <div class="row"><div class="ph light" style="position:relative;width:34px;height:34px" role="img" aria-label="Team member portrait"></div><div><div class="h">Name Here</div><div class="p">Job title</div></div></div>
    <div class="row"><div class="ph light" style="position:relative;width:34px;height:34px" role="img" aria-label="Team member portrait"></div><div><div class="h">Name Here</div><div class="p">Job title</div></div></div>
  </div>
  <div class="foot"></div>
</section>

<section class="slide">
  <div class="title">Your Blank Slide</div><div class="brand"><i></i>BRIGHTVALE</div>
  <div class="abs row" style="left:200px;top:90px;opacity:.12"><i style="display:block;width:24px;height:24px;background:var(--ink)"></i><span style="font-size:18px;letter-spacing:3px">BRIGHTVALE</span></div>
  <div class="foot"></div>
</section>

<!-- row 15 -->
<section class="slide">
  <div class="title">Customer Testimonials</div><div class="brand"><i></i>BRIGHTVALE</div>
  <div class="ph light" style="left:40px;top:40px;width:40px;height:50px" role="img" aria-label="Customer portrait"></div>
  <div class="abs" style="left:0;right:0;top:100px;height:80px;background:var(--ink)"></div>
  <div class="abs" style="left:20px;top:112px;width:100px;font-size:5.5px;line-height:1.5;color:#ccc">“A short client quote about the mentoring goes here.”</div>
  <div class="abs" style="left:140px;top:112px;width:100px;font-size:5.5px;line-height:1.5;color:#ccc">“A short client quote about the mentoring goes here.”</div>
  <div class="abs" style="left:260px;top:112px;width:100px;font-size:5.5px;line-height:1.5;color:#ccc">“A short client quote about the mentoring goes here.”</div>
  <div class="foot"></div>
</section>

<section class="slide">
  <div class="title">Financial Report</div><div class="brand"><i></i>BRIGHTVALE</div>
  <svg class="abs" style="left:30px;top:50px" width="110" height="90" viewBox="0 0 110 90">
    <ellipse cx="55" cy="45" rx="52" ry="40" fill="#1a1a1a"/>
    <path d="M55 45 L55 5 A52 40 0 0 1 107 45Z" fill="#7dc0bb"/>
    <path d="M55 45 L107 45 A52 40 0 0 1 80 80Z" fill="#8c8c8c"/>
  </svg>
  <div class="abs" style="left:30px;top:160px;font-size:14px;color:var(--teal)">54%</div>
  <div class="abs" style="left:200px;top:54px;display:flex;flex-direction:column;gap:14px">
    <div class="row"><i class="sq"></i><div><div class="h">Your Text Here</div><div class="p">Short text</div></div></div>
    <div class="row"><i class="sq" style="background:var(--ink)"></i><div><div class="h">Your Text Here</div><div class="p">Short text</div></div></div>
    <div class="row"><i class="sq" style="background:var(--grey)"></i><div><div class="h">Your Text Here</div><div class="p">Short text</div></div></div>
  </div>
  <div class="foot"></div>
</section>

<section class="slide">
  <div class="title">Bullet &amp; Chart Area</div><div class="brand"><i></i>BRIGHTVALE</div>
  <svg class="abs" style="left:20px;top:46px" width="200" height="130" viewBox="0 0 200 130">
    <g fill="#1a1a1a"><rect x="0" y="5" width="150" height="10"/><rect x="0" y="40" width="120" height="10"/><rect x="0" y="75" width="170" height="10"/><rect x="0" y="110" width="90" height="10"/></g>
    <g fill="#7dc0bb"><rect x="0" y="17" width="100" height="10"/><rect x="0" y="52" width="160" height="10"/><rect x="0" y="87" width="70" height="10"/><rect x="0" y="122" width="130" height="8"/></g>
  </svg>
  <div class="abs" style="left:244px;top:54px;display:flex;flex-direction:column;gap:14px">
    <div class="row"><i class="sq"></i><div><div class="h">Category One</div><div class="p">Short text</div></div></div>
    <div class="row"><i class="sq" style="background:var(--ink)"></i><div><div class="h">Category Two</div><div class="p">Short text</div></div></div>
    <div class="row"><i class="sq" style="background:var(--grey)"></i><div><div class="h">Category Three</div><div class="p">Short text</div></div></div>
  </div>
  <div class="foot"></div>
</section>

<!-- row 16 -->
<section class="slide">
  <div class="title">Infographic</div><div class="brand"><i></i>BRIGHTVALE</div>
  <svg class="abs" style="left:30px;top:44px" width="150" height="140" viewBox="0 0 150 140">
    <path d="M75 5 L100 45 L50 45Z" fill="#1a1a1a"/>
    <path d="M48 49 L102 49 L125 88 L25 88Z" fill="#7dc0bb"/>
    <path d="M23 92 L127 92 L150 135 L0 135Z" fill="#4a4a4a"/>
  </svg>
  <div class="abs" style="left:210px;top:54px;display:flex;flex-direction:column;gap:16px">
    <div class="row"><i class="sq" style="background:var(--ink)"></i><div><div class="h">Content Title</div><div class="p">Short text</div></div></div>
    <div class="row"><i class="sq"></i><div><div class="h">Content Title</div><div class="p">Short text</div></div></div>
    <div class="row"><i class="sq" style="background:var(--slate)"></i><div><div class="h">Content Title</div><div class="p">Short text</div></div></div>
  </div>
  <div class="foot"></div>
</section>

<section class="slide">
  <div class="title">Digital System</div><div class="brand"><i></i>BRIGHTVALE</div>
  <svg class="abs" style="left:143px;top:46px" width="100" height="100" viewBox="0 0 100 100">
    <g fill="none" stroke-width="18">
      <circle cx="50" cy="50" r="38" stroke="#1a1a1a"/>
      <path d="M50 12 A38 38 0 0 1 88 50" stroke="#7dc0bb"/>
      <path d="M50 88 A38 38 0 0 1 12 50" stroke="#8c8c8c"/>
    </g>
  </svg>
  <div class="abs" style="left:30px;top:56px"><div class="h">Your Text</div><div class="p">Short text</div></div>
  <div class="abs" style="left:30px;top:120px"><div class="h">Your Text</div><div class="p">Short text</div></div>
  <div class="abs" style="left:280px;top:56px"><div class="h">Your Text</div><div class="p">Short text</div></div>
  <div class="abs" style="left:280px;top:120px"><div class="h">Your Text</div><div class="p">Short text</div></div>
  <div class="foot"></div>
</section>

<section class="slide">
  <div class="title">Advanced</div><div class="brand"><i></i>BRIGHTVALE</div>
  <svg class="abs" style="left:140px;top:46px" width="106" height="106" viewBox="0 0 106 106">
    <path d="M0 50 A50 50 0 0 1 50 0 L50 50Z" fill="#1a1a1a"/>
    <path d="M56 0 A50 50 0 0 1 106 50 L56 50Z" fill="#8c8c8c"/>
    <path d="M106 56 A50 50 0 0 1 56 106 L56 56Z" fill="#1a1a1a"/>
    <path d="M50 106 A50 50 0 0 1 0 56 L50 56Z" fill="#7dc0bb"/>
  </svg>
  <div class="abs" style="left:30px;top:56px"><div class="h">Your Text</div><div class="p">Short text</div></div>
  <div class="abs" style="left:30px;top:124px"><div class="h">Your Text</div><div class="p">Short text</div></div>
  <div class="abs" style="left:280px;top:56px"><div class="h">Your Text</div><div class="p">Short text</div></div>
  <div class="abs" style="left:280px;top:124px"><div class="h">Your Text</div><div class="p">Short text</div></div>
  <div class="foot"></div>
</section>

<!-- row 17 -->
<section class="slide">
  <div class="title">About Us</div><div class="brand"><i></i>BRIGHTVALE</div>
  <div class="ph light dot" style="left:158px;top:40px;width:70px;height:70px" role="img" aria-label="Round portrait of the founder"></div>
  <div class="abs" style="left:0;right:0;top:118px;text-align:center"><div class="h">Owen</div><div class="p" style="width:260px;margin:4px auto 0">A short biography paragraph about the founder and the mentoring approach goes here.</div></div>
  <div class="abs" style="left:168px;top:176px;display:flex;gap:6px"><i class="dot" style="width:10px;height:10px;background:var(--teal)"></i><i class="dot" style="width:10px;height:10px;background:var(--teal)"></i><i class="dot" style="width:10px;height:10px;background:var(--teal)"></i></div>
  <div class="foot"></div>
</section>

<section class="slide">
  <div class="title">Europe Map</div><div class="brand"><i></i>BRIGHTVALE</div>
  <div class="abs" style="left:40px;top:40px;width:200px;height:140px;background:radial-gradient(ellipse at 50% 50%,#7dc0bb 0%,#4a4a4a 60%,transparent 72%)" role="img" aria-label="Map of Europe with highlighted countries"></div>
  <div class="abs" style="left:260px;top:60px;display:flex;flex-direction:column;gap:12px">
    <div class="row"><i class="sq"></i><span class="p">Text Here</span></div>
    <div class="row"><i class="sq" style="background:var(--ink)"></i><span class="p">Text Here</span></div>
    <div class="row"><i class="sq" style="background:var(--grey)"></i><span class="p">Text Here</span></div>
  </div>
  <div class="foot"></div>
</section>

<section class="slide">
  <div class="title">Global Experience</div><div class="brand"><i></i>BRIGHTVALE</div>
  <div class="abs" style="left:20px;top:50px;width:346px;height:130px;background:radial-gradient(ellipse at 50% 50%,#cfcfcf 0%,#e8e8e8 55%,transparent 72%)" role="img" aria-label="Grey world map"></div>
  <div class="abs p" style="left:80px;top:76px;color:var(--ink)">North America</div>
  <div class="abs p" style="left:200px;top:70px;color:var(--ink)">Europe</div>
  <div class="abs p" style="left:290px;top:86px;color:var(--ink)">Asia</div>
  <div class="foot"></div>
</section>

<!-- row 18 -->
<section class="slide">
  <div class="title">Table Area</div><div class="brand"><i></i>BRIGHTVALE</div>
  <div class="abs" style="left:40px;top:44px;width:306px;display:grid;grid-template-columns:2fr 1fr 1fr;font-size:6px;gap:2px">
    <div style="background:var(--ink);color:#fff;padding:4px">Description</div><div style="background:var(--teal);color:#fff;padding:4px">Column 1</div><div style="background:var(--slate);color:#fff;padding:4px">Column 2</div>
    <div style="padding:4px;border-bottom:1px solid var(--mist)">Row Item 1</div><div style="padding:4px;border-bottom:1px solid var(--mist)">✔</div><div style="padding:4px;border-bottom:1px solid var(--mist)">✔</div>
    <div style="padding:4px;border-bottom:1px solid var(--mist)">Row Item 2</div><div style="padding:4px;border-bottom:1px solid var(--mist)">✔</div><div style="padding:4px;border-bottom:1px solid var(--mist)">—</div>
    <div style="padding:4px;border-bottom:1px solid var(--mist)">Row Item 3</div><div style="padding:4px;border-bottom:1px solid var(--mist)">—</div><div style="padding:4px;border-bottom:1px solid var(--mist)">✔</div>
    <div style="padding:4px;border-bottom:1px solid var(--mist)">Row Item 4</div><div style="padding:4px;border-bottom:1px solid var(--mist)">✔</div><div style="padding:4px;border-bottom:1px solid var(--mist)">✔</div>
    <div style="padding:4px">Row Item 5</div><div style="padding:4px">✔</div><div style="padding:4px">—</div>
  </div>
  <div class="foot"></div>
</section>

<section class="slide">
  <div class="title">Bullet &amp; Chart Area</div><div class="brand"><i></i>BRIGHTVALE</div>
  <div class="abs" style="left:20px;top:50px;display:flex;flex-direction:column;gap:12px">
    <div class="row"><i class="sq"></i><span class="p">Your Text Here</span></div>
    <div class="row"><i class="sq"></i><span class="p">Your Text Here</span></div>
    <div class="row"><i class="sq"></i><span class="p">Your Text Here</span></div>
    <div class="row"><i class="sq"></i><span class="p">Your Text Here</span></div>
  </div>
  <svg class="abs" style="left:170px;top:60px" width="80" height="80" viewBox="0 0 80 80">
    <circle cx="40" cy="40" r="32" fill="none" stroke="#e4e4e4" stroke-width="12"/>
    <path d="M40 8 A32 32 0 1 1 21.2 65.9" fill="none" stroke="#7dc0bb" stroke-width="12"/>
  </svg>
  <div class="abs" style="left:300px;top:92px;font-size:14px">60%</div>
  <div class="foot"></div>
</section>

<section class="slide dark">
  <div class="ph warm" style="inset:0" role="img" aria-label="Dark room with light bulbs"></div>
  <div class="abs row" style="left:150px;top:18px"><i class="sq"></i><span style="font-size:9px;letter-spacing:2px">BRIGHTVALE</span></div>
  <div class="abs" style="left:20px;top:70px;font-size:11px">Our Contact</div>
  <div class="abs" style="left:20px;top:92px;display:flex;flex-direction:column;gap:7px;font-size:5.5px;color:#ccc">
    <div class="row"><i class="dot" style="width:8px;height:8px;background:var(--teal)"></i>0100 000 0000</div>
    <div class="row"><i class="dot" style="width:8px;height:8px;background:var(--teal)"></i>info@brightvalementoring.co.uk</div>
    <div class="row"><i class="dot" style="width:8px;height:8px;background:var(--teal)"></i>www.brightvalementoring.co.uk</div>
  </div>
  <div class="abs" style="left:250px;top:150px;font-size:16px;letter-spacing:1px">THANK YOU</div>
  <div class="abs p" style="left:250px;top:172px;width:120px">Short closing line of text here</div>
  <div class="abs" style="left:165px;top:200px;display:flex;gap:5px"><i class="dot" style="width:8px;height:8px;background:var(--teal)"></i><i class="dot" style="width:8px;height:8px;background:var(--teal)"></i><i class="dot" style="width:8px;height:8px;background:var(--teal)"></i></div>
</section>

</main>
</body>
</html>
```